Coaching and Products Website- with possible booking and payment functionality

https://bemonavrek.example.com/mysite-1/home
Would like to maintain unique feel, clear Clean uncluttered ui design.
With Booking and payment functionality if possible.
Please send any examples of prior booking sites you have done and what plugin, widgets, or 3rd party used for this functionality.
Thank you!

Target Market(s)

People interested in coaching and health and fitness products

Number of Pages Required

5+ page

Requirements
Must have
• Would like to use existing content to build a site with a few coaches in the Orange County, CA area to start with ability to login, pay and book different coaches like on trainvex.com or ourpaddlecourse.com.
• Can be done on wordpress or suggest platform please

```html
<!DOCTYPE html>
<html lang="en">
<head>
<meta charset="utf-8">
<title>Courtline Tennis Training</title>
<link href="https://fonts.googleapis.com/css2?family=Montserrat:wght@400;600;700;800&family=Open+Sans:wght@400;600;700&display=swap" rel="stylesheet">
<style>
:root{
  --green:#7dad2f;
  --green-dark:#3c5b1f;
  --lime:#cfd92c;
  --teal:#1e9b74;
  --ink:#1f1f1f;
  --charcoal:#2f2f2f;
  --grey-bg:#f3f1f1;
  --text:#333;
  --white:#fff;
}
*{margin:0;padding:0;box-sizing:border-box}
html,body{width:1200px;height:3727px;overflow:hidden}
body{position:relative;background:var(--white);font-family:'Open Sans',sans-serif;color:var(--text)}
.abs{position:absolute}

/* header */
.site-header{left:0;top:0;width:1200px;height:100px}
.brand{left:120px;top:24px;display:flex;align-items:center;gap:12px;font-family:'Montserrat',sans-serif;font-weight:600;font-size:30px;color:var(--ink)}
.brand-dot{width:22px;height:22px;border-radius:50%;background:var(--lime)}
.nav{left:706px;top:40px;display:flex;gap:40px;font-family:'Montserrat',sans-serif;font-weight:700;font-size:12px;color:var(--ink)}
.nav .active{color:var(--green);border-bottom:3px solid var(--green);padding-bottom:6px}

/* hero */
.hero{left:0;top:100px;width:1200px;height:595px;background:linear-gradient(120deg,#3f6fa6 0%,#7fa7cf 30%,#c8c2b4 55%,#c76a3c 80%,#a7502b 100%)}
.hero-box{left:50px;top:367px;width:402px;height:174px;background:rgba(40,40,40,.72);padding:22px 32px}
.hero-box h1{font-family:'Montserrat',sans-serif;font-weight:800;font-size:31px;line-height:36px;color:var(--white)}
.btn{display:inline-block;background:var(--green);color:var(--white);font-family:'Montserrat',sans-serif;font-weight:700;font-size:12px;text-align:center}
.hero-box .btn{margin-top:16px;padding:12px 22px;font-size:13px}
.dots{left:552px;top:650px;display:flex;gap:11px}
.dots span{width:8px;height:8px;border-radius:50%;background:rgba(255,255,255,.6)}
.dots span.on{background:var(--white);box-shadow:0 0 0 2px #333}

/* lessons */
.section-title{width:1200px;left:0;text-align:center;font-family:'Montserrat',sans-serif;font-weight:700;font-size:24px;color:var(--ink)}
.rule{left:570px;width:60px;height:2px;background:#ccc}
.lesson{top:857px;width:256px;text-align:center}
.lesson .photo{height:311px;width:256px}
.lesson h3{margin-top:30px;font-family:'Montserrat',sans-serif;font-weight:700;font-size:13px;color:var(--ink)}
.price{margin-top:12px;display:flex;justify-content:center;align-items:center;gap:10px;font-family:'Montserrat',sans-serif;font-weight:700;font-size:24px;color:var(--ink)}
.tag{background:#333;color:var(--white);font-size:11px;padding:3px 8px}
.lesson .btn{margin-top:18px;padding:8px 16px;font-size:11px}
.view-all{left:546px;top:1368px;width:108px;height:34px;line-height:34px;background:var(--ink);color:var(--white);font-family:'Montserrat',sans-serif;font-weight:700;font-size:13px;text-align:center}

/* testimonials */
.testimonials{left:0;top:1495px;width:1200px;height:530px;background:linear-gradient(90deg,#c26f43 0%,#d08457 40%,#b85f35 100%)}
.quotes{left:132px;top:1495px;width:365px;height:530px;background:var(--green);padding:44px 38px 0 40px;color:var(--white)}
.mark{font-family:Georgia,serif;font-weight:700;font-size:34px;line-height:24px}
.quote p{font-size:14.5px;line-height:20px;margin-top:4px}
.quote cite{display:block;margin-top:14px;font-style:normal;font-weight:700;font-size:14px}
.divider{width:70px;height:1px;background:rgba(255,255,255,.7);margin:18px 0 26px}

/* welcome */
.welcome-band{left:0;top:2025px;width:1200px;height:452px;background:var(--grey-bg)}
.welcome-kicker{left:0;top:2092px;width:1200px;text-align:center;font-family:'Montserrat',sans-serif;font-weight:700;font-size:16px;color:var(--ink)}
.welcome-title{left:0;top:2118px;width:1200px;text-align:center;font-family:'Montserrat',sans-serif;font-weight:700;font-size:31px;letter-spacing:1px;color:var(--ink)}
.welcome-lead{left:370px;top:2184px;width:460px;text-align:center;font-size:15px;line-height:22px}
.motto{top:2312px;width:240px;font-family:'Montserrat',sans-serif;font-weight:800;font-size:14px;line-height:17px;color:var(--ink)}
.bar{top:2304px;width:3px;height:50px;background:var(--green)}
.welcome-btn{left:537px;top:2396px;width:126px;height:34px;line-height:34px;font-size:13px}

/* store grid */
.cell{width:300px;height:345px}
.book{padding:80px 28px 0 30px;color:var(--white)}
.book h4{font-family:'Montserrat',sans-serif;font-weight:600;font-size:18px;line-height:22px}
.book .cost{margin-top:24px;font-family:'Montserrat',sans-serif;font-weight:700;font-size:28px}
.buy{display:flex;align-items:center;gap:8px;margin-top:22px;width:186px;height:42px;justify-content:center;background:var(--green);color:var(--white);font-family:'Montserrat',sans-serif;font-weight:700;font-size:13px}
.buy i{width:10px;height:10px;background:var(--white)}
.buy.light{background:var(--white);color:var(--green)}
.buy.light i{background:var(--green)}
.mission{padding:70px 60px 0 60px;color:var(--white)}
.mission h4{font-family:'Montserrat',sans-serif;font-weight:800;font-size:22px}
.mission p{margin-top:18px;font-size:14px;line-height:18px}
.mission .more{display:inline-block;margin-top:22px;background:var(--white);color:var(--ink);font-family:'Montserrat',sans-serif;font-weight:700;font-size:11px;padding:7px 15px}

/* footer */
.foot-h{font-family:'Montserrat',sans-serif;font-weight:700;font-size:15px;color:var(--ink)}
.menu-list{list-style:none;font-size:12.5px;line-height:17.5px;color:var(--ink)}
.contact-row{display:flex;gap:16px;align-items:flex-start;font-size:12px;color:#555}
.contact-row b{display:block;font-family:'Montserrat',sans-serif;font-weight:700;font-size:14px;color:var(--ink)}
.social{display:flex;flex-direction:column;gap:4px;font-size:12px;font-weight:600;color:var(--ink)}
.social span{display:flex;align-items:center;gap:4px}
.social i{width:10px;height:10px;border-radius:50%;background:#2b6cb0}
.newsletter-input{left:442px;top:3498px;width:406px;height:37px;border:1px solid #bbb;padding:10px 12px;font-size:12px;color:#555}
.join{left:442px;top:3547px;width:406px;height:43px;line-height:43px;background:var(--green);color:var(--white);text-align:center;font-family:'Montserrat',sans-serif;font-weight:700;font-size:20px}
.copyright{left:0;width:1200px;top:3682px;text-align:center;font-size:11px;color:var(--ink)}
</style>
</head>
<body>

<header class="abs site-header">
  <div class="abs brand"><span class="brand-dot"></span>Courtline Tennis training</div>
  <nav class="abs nav"><span class="active">HOME</span><span>ABOUT</span><span>LESSONS</span><span>STORE</span><span>CONTACT</span></nav>
</header>

<section class="abs hero" role="img" aria-label="Photo of a tennis player hitting a ball close to the racket on a clay court"></section>
<div class="abs hero-box">
  <h1>TAKE YOUR TENNIS<br>TO THE NEXT LEVEL</h1>
  <span class="btn">READ MORE &#8250;</span>
</div>
<div class="abs dots"><span></span><span></span><span class="on"></span><span></span></div>

<h2 class="abs section-title" style="top:750px">LESSONS</h2>
<div class="abs rule" style="top:800px"></div>

<div class="abs lesson" style="left:32px">
  <div class="photo" role="img" aria-label="Player on a green hard court" style="background:linear-gradient(180deg,#2f5a3c,#4e7d57)"></div>
  <h3>TENNIS BY THE SESSION</h3>
  <div class="price">$75.00 <span class="tag">1 HR</span></div>
  <span class="btn">BOOK NOW</span>
</div>
<div class="abs lesson" style="left:325px">
  <div class="photo" role="img" aria-label="Player serving outdoors among trees" style="background:linear-gradient(180deg,#6d8fb8,#5d7a3a 60%,#7e6a4d)"></div>
  <h3>TENNIS PACKAGE OF 6 LESSONS</h3>
  <div class="price">$450.00 <span class="tag">1 HR</span></div>
  <span class="btn">BOOK NOW</span>
</div>
<div class="abs lesson" style="left:618px">
  <div class="photo" role="img" aria-label="Player swinging on a blue court" style="background:linear-gradient(180deg,#2d62b8,#3a78c8)"></div>
  <h3>TENNIS 12 SESSIONS</h3>
  <div class="price">$840.00 <span class="tag">1 HR</span></div>
  <span class="btn">BOOK NOW</span>
</div>
<div class="abs lesson" style="left:907px">
  <div class="photo" role="img" aria-label="Two players' feet on a clay court" style="background:linear-gradient(180deg,#8c8a6a,#a4603f 40%,#9c5335)"></div>
  <h3>TENNIS IN PAIRS</h3>
  <div class="price">$80.00 <span class="tag">1 HR</span></div>
  <span class="btn">BOOK NOW</span>
</div>
<div class="abs view-all">VIEW ALL</div>

<section class="abs testimonials" role="img" aria-label="Photo of a player lunging for a forehand on clay"></section>
<div class="abs quotes">
  <div class="quote">
    <div class="mark">&#8220;</div>
    <p>Coach Elena is amazing! My daughter connected well with her. She doesn't waste time and challenges you. She has a professional approach that enables my daughter to absorb critiques while having a respectful relationship!</p>
    <cite>Tomas R.</cite>
  </div>
  <div class="divider"></div>
  <div class="quote">
    <div class="mark">&#8220;</div>
    <p>Coach Elena is awesome! She is very thoughtful about training planning, and very patient and encouraging toward my daughter Lily. We would highly recommend coach Elena to any parents or group looking for a great Tennis Coach.</p>
    <cite>Derek W</cite>
  </div>
</div>

<section class="abs welcome-band"></section>
<div class="abs welcome-kicker">WELCOME TO</div>
<h2 class="abs welcome-title">COURTLINE TENNIS TRAINING</h2>
<p class="abs welcome-lead">We provide Coaching, Tennis Lessons and Training in Orange County, CA.Skilled Tennis professionals are available 7 days a week guaranteeing you a greater game,hus giving you the focus required for a more enjoyable and competitive edge.</p>
<div class="abs motto" style="left:240px">PRACTICE HARD. PLAY WELL. BE A WINNER.</div>
<div class="abs bar" style="left:489px"></div>
<div class="abs motto" style="left:517px">WHEN YOU PRACTICE HARD, YOU'LL PLAY WELL.</div>
<div class="abs bar" style="left:764px"></div>
<div class="abs motto" style="left:793px">IT'S TIME TO ESTABLISH YOUR GAME.</div>
<span class="abs btn welcome-btn">READ MORE</span>

<div class="abs cell" style="left:0;top:2477px;background:var(--lime)">
  <div role="img" aria-label="Book cover of Relentless, portrait of the author" style="margin:20px 0 0 55px;width:192px;height:307px;background:linear-gradient(180deg,#f0f0ee,#9a9a98)"></div>
</div>
<div class="abs cell book" style="left:300px;top:2477px;background:var(--green-dark)">
  <h4>Relentless:<br>Notes From the Baseline</h4>
  <div class="cost">$ 12.55</div>
  <div class="buy"><i></i>BUY ON SHOPMARKET</div>
</div>
<div class="abs cell" style="left:600px;top:2477px;background:var(--white)">
  <div role="img" aria-label="Book cover of The Quiet Court with a tennis ball" style="margin:0 auto;width:220px;height:345px;background:radial-gradient(circle at 50% 22%,#e4e63a 0,#cfd22a 55px,#fafaf6 70px,#f3f1e8 100%)"></div>
</div>
<div class="abs cell book" style="left:900px;top:2477px;background:var(--charcoal);padding-top:56px">
  <h4>The Quiet Court: The Classic Guide to the Mental Side of Peak Performance</h4>
  <div class="cost" style="margin-top:18px">$ 11.55</div>
  <div class="buy"><i></i>BUY ON SHOPMARKET</div>
</div>

<div class="abs cell book" style="left:0;top:2822px;background:var(--green);padding-top:92px">
  <h4>Point by Point: The 14-Day Clean-Eating Plan for Physical and Mental Excellence</h4>
  <div class="cost">$ 14.35</div>
  <div class="buy light"><i></i>BUY ON SHOPMARKET</div>
</div>
<div class="abs cell" style="left:300px;top:2822px;background:var(--white)">
  <div role="img" aria-label="Book cover of Point by Point with the author in white" style="margin:10px auto 0;width:250px;height:335px;background:linear-gradient(180deg,#f4f4f4,#d9dde2 70%,#c8ccd2)"></div>
</div>
<div class="abs cell mission" style="left:600px;top:2822px;background:var(--teal)">
  <h4>MISSION</h4>
  <p>Lorem ipsum is simply dummy text of the printing and typesetting industry. Lorem Ipsum has been the industry's standard dummy text ever since the.</p>
  <span class="more">READ MORE</span>
</div>
<div class="abs cell" role="img" aria-label="Player serving on a court at sunset" style="left:900px;top:2822px;background:linear-gradient(180deg,#2a1a14,#b8451c 45%,#f08a2a 65%,#3a5a2a 85%)"></div>

<div class="abs" role="img" aria-label="Large tennis ball graphic" style="left:-25px;top:3341px;width:422px;height:422px;border-radius:50%;background:var(--lime)"></div>

<div class="abs foot-h" style="left:380px;top:3230px">MENU</div>
<ul class="abs menu-list" style="left:380px;top:3262px"><li>Home</li><li>About</li><li>Lessons</li><li>Store</li><li>Contact</li></ul>

<div class="abs foot-h" style="left:623px;top:3230px">CONTACT US</div>
<div class="abs contact-row" style="left:623px;top:3270px">
  <svg width="16" height="16" viewBox="0 0 24 24"><path fill="#555" d="M6.6 10.8a15 15 0 0 0 6.6 6.6l2.2-2.2a1 1 0 0 1 1-.25 11.4 11.4 0 0 0 3.6.57 1 1 0 0 1 1 1V20a1 1 0 0 1-1 1A17 17 0 0 1 3 4a1 1 0 0 1 1-1h3.5a1 1 0 0 1 1 1c0 1.25.2 2.45.57 3.57a1 1 0 0 1-.25 1z"/></svg>
  <div>CALL US<b>949-555-0172</b></div>
</div>
<div class="abs contact-row" style="left:623px;top:3320px">
  <svg width="16" height="16" viewBox="0 0 24 24"><rect x="2" y="5" width="20" height="14" fill="#555"/><path d="M2 5l10 8 10-8" stroke="#fff" stroke-width="1.6" fill="none"/></svg>
  <div>E MAIL US<b>coach@courtline-mail.example</b></div>
</div>

<div class="abs foot-h" style="left:961px;top:3230px">FOLLOW US</div>
<div class="abs social" style="left:961px;top:3266px">
  <span><i></i>Pagebook</span><span><i></i>Chirper</span><span><i></i>Linkwork</span>
</div>

<div class="abs foot-h" style="left:442px;top:3458px">NEWSLETTER SUBSCRIBE</div>
<div class="abs newsletter-input">E Mail Address</div>
<div class="abs join">JOIN NOW</div>

<div class="abs copyright">Copyrights @ 2019 All Rights Reserved</div>

</body>
</html>
```